Business cards for KORU Real Estate Holdings LLC

We need a cool, original business card design for a company based in the Washington DC metropolitan area. We are a new energetic and passionate Real Estate Investing Company that invests in all types of real estate; commercial, residential, industrial etc.

Our company color is Red since it reflects action, energy and speed; it is assertive confident, energizing, exciting, powerful, passionate and determined. So we would like business card communicate those qualities to the audience.

Our audiences are investors that want to invest with us, real estate sellers, buyers, and tenants who lease from us.

Our logo is attached

```html
<!DOCTYPE html>
<html lang="en">
<head>
<meta charset="utf-8">
<title>KORU Real Estate Holdings LLC — Business Cards</title>
<link href="https://fonts.googleapis.com/css2?family=Lato:wght@400;700;900&display=swap" rel="stylesheet">
<style>
  :root {
    --bg: #e9e6e2;
    --card-dark: #3b3b3d;
    --card-dark-hi: #4a4a4d;
    --card-light: #ffffff;
    --ink: #2b2b2e;
    --ink-soft: #4a4a50;
    --red: #c8202a;
    --grey-band: #3d3d40;
    --line: #6b6b70;
    --white: #ffffff;
  }
  * { margin: 0; padding: 0; box-sizing: border-box; }
  html, body {
    width: 1200px; height: 891px; overflow: hidden;
    background: var(--bg);
    font-family: 'Lato', sans-serif;
  }
  .canvas { position: relative; width: 1200px; height: 891px; }

  .card {
    position: absolute;
    width: 640px; height: 366px;
    box-shadow: 0 14px 30px rgba(0,0,0,.22);
  }

  /* Back side */
  .card--back {
    left: 110px; top: 55px;
    background: linear-gradient(100deg, var(--card-dark) 0%, var(--card-dark-hi) 50%, var(--card-dark) 100%);
  }
  .back-brand {
    position: absolute; right: 70px; top: 120px;
    display: flex; align-items: center; gap: 16px;
  }
  .brand-dot {
    width: 44px; height: 44px; border-radius: 50%;
    background: var(--red); flex: none;
  }
  .brand-name {
    font-weight: 900; color: var(--white);
    line-height: 1.05;
  }
  .brand-name .big { display: block; font-size: 58px; letter-spacing: 4px; }
  .brand-name .small { display: block; font-size: 13.5px; letter-spacing: 1px; }
  .back-web {
    position: absolute; right: 70px; top: 245px;
    color: var(--white); font-size: 17px; letter-spacing: 3px;
  }

  /* Front side */
  .card--front {
    left: 450px; top: 470px;
    background: var(--card-light);
    overflow: hidden;
  }
  .front-brand {
    position: absolute; left: 40px; top: 190px;
    display: flex; align-items: center; gap: 12px;
  }
  .front-brand .brand-name { color: var(--ink); }
  .front-brand .brand-name .big { font-size: 46px; letter-spacing: 3px; }
  .front-brand .brand-name .small { font-size: 11px; letter-spacing: .8px; }
  .front-brand .brand-dot { width: 36px; height: 36px; }

  .divider {
    position: absolute; left: 330px; top: 95px;
    width: 1px; height: 175px; background: var(--line);
  }
  .details { position: absolute; left: 352px; top: 96px; color: var(--ink); }
  .person-name { font-size: 21px; font-weight: 900; letter-spacing: -.3px; }
  .person-title { font-size: 14px; font-weight: 700; margin-top: 1px; }
  .address { font-size: 13px; color: var(--ink-soft); margin-top: 22px; line-height: 1.35; }
  .contact-grid {
    display: grid; grid-template-columns: auto auto;
    column-gap: 22px; row-gap: 5px; margin-top: 16px;
    font-size: 13px; color: var(--ink-soft);
  }
  .contact { display: flex; align-items: center; gap: 7px; }
  .contact svg { width: 13px; height: 13px; flex: none; fill: var(--ink); }

  .band {
    position: absolute; left: 0; bottom: 0; width: 100%; height: 16px;
    display: flex;
  }
  .band span { height: 100%; }
  .band .red-a { flex: 45; background: var(--red); }
  .band .grey { flex: 30; background: var(--grey-band); }
  .band .red-b { flex: 25; background: var(--red); }
</style>
</head>
<body>
<main class="canvas">

  <section class="card card--back" aria-label="Card back">
    <div class="back-brand">
      <span class="brand-dot"></span>
      <span class="brand-name"><span class="big">KORU</span><span class="small">REAL ESTATE HOLDINGS LLC</span></span>
    </div>
    <p class="back-web">www.koruholdings.com</p>
  </section>

  <section class="card card--front" aria-label="Card front">
    <div class="front-brand">
      <span class="brand-dot"></span>
      <span class="brand-name"><span class="big">KORU</span><span class="small">REAL ESTATE HOLDINGS LLC</span></span>
    </div>

    <div class="divider"></div>

    <div class="details">
      <h1 class="person-name">MARCUS HALE</h1>
      <p class="person-title">Founder</p>
      <p class="address">Address 1820 Riverside Parkway,<br>Suite 200, Arlington, VA 22201</p>
      <div class="contact-grid">
        <span class="contact">
          <svg viewBox="0 0 24 24" aria-hidden="true"><path d="M6.6 10.8a15 15 0 0 0 6.6 6.6l2.2-2.2a1 1 0 0 1 1-.25 11.4 11.4 0 0 0 3.6.57 1 1 0 0 1 1 1V20a1 1 0 0 1-1 1A17 17 0 0 1 3 4a1 1 0 0 1 1-1h3.5a1 1 0 0 1 1 1c0 1.25.2 2.45.57 3.57a1 1 0 0 1-.25 1z"/></svg>
          555 310 0148
        </span>
        <span class="contact">
          <svg viewBox="0 0 24 24" aria-hidden="true"><path d="M2 5h20v14H2zm2 2v.5l8 5 8-5V7zm0 2.8V17h16V9.8l-8 5z"/></svg>
          info@koruholdings.com
        </span>
        <span class="contact">
          <svg viewBox="0 0 24 24" aria-hidden="true"><path d="M7 1h10a2 2 0 0 1 2 2v18a2 2 0 0 1-2 2H7a2 2 0 0 1-2-2V3a2 2 0 0 1 2-2zm0 3v14h10V4zm5 15.2a1.2 1.2 0 1 0 0 2.4 1.2 1.2 0 0 0 0-2.4z"/></svg>
          555 310 0148
        </span>
        <span class="contact">
          <svg viewBox="0 0 24 24" aria-hidden="true"><path d="M12 2a10 10 0 1 0 0 20 10 10 0 0 0 0-20zm7.9 9h-3.5a15 15 0 0 0-1.3-6.2A8 8 0 0 1 19.9 11zM12 4c.9 1.2 2.2 3.6 2.4 7H9.6c.2-3.4 1.5-5.8 2.4-7zM8.9 4.8A15 15 0 0 0 7.6 11H4.1a8 8 0 0 1 4.8-6.2zM4.1 13h3.5a15 15 0 0 0 1.3 6.2A8 8 0 0 1 4.1 13zm7.9 7c-.9-1.2-2.2-3.6-2.4-7h4.8c-.2 3.4-1.5 5.8-2.4 7zm3.1-.8a15 15 0 0 0 1.3-6.2h3.5a8 8 0 0 1-4.8 6.2z"/></svg>
          www.koruholdings.com
        </span>
      </div>
    </div>

    <div class="band" aria-hidden="true">
      <span class="red-a"></span><span class="grey"></span><span class="red-b"></span>
    </div>
  </section>

</main>
</body>
</html>
```